Holvern Incorporated

Holvern is a business that provides consulting, and manages and supplies trades persons in the construction and heavy industries sector. We build, do maintenance, install machinery, and can manage projects or jobs. Would like or prefer more clean, classic designs. Blacks/greys, but open to almost anything.

Target Market(s)

Industrial/Construction/Manufacturing

Industry/Entity Type

Construction Company

Contact Information for Business Card

Clean, business name on the front, possibly have the details on the back, but open to any ideas.

Logo Text

We currently do not have a slogan, open to ideas

Font styles to use
Serif
Sans Serif

Colors

Designer to choose colors to be used in the design.

Requirements
Should not have
• the oval is not my logo, was just an idea. please don't send 20 designs with the oval

```html
<!DOCTYPE html>
<html lang="en">
<head>
<meta charset="utf-8">
<title>Holvern Incorporated — Business Card</title>
<link href="https://fonts.googleapis.com/css2?family=Open+Sans:wght@400;600&display=swap" rel="stylesheet">
<style>
  :root {
    --backdrop: #d6d6d6;
    --card-black: #0b0b0b;
    --card-white: #ffffff;
    --ink-light: #ffffff;
    --ink-dark: #1a1a1a;
    --emboss: #262626;
    --icon: #555555;
  }
  * { margin: 0; padding: 0; box-sizing: border-box; }
  html, body {
    width: 1200px; height: 900px; overflow: hidden;
    background: var(--backdrop);
    font-family: "Open Sans", sans-serif;
  }
  .stage {
    width: 1200px; height: 900px;
    display: flex; align-items: center; justify-content: center; gap: 60px;
  }
  .card {
    width: 520px; height: 300px; position: relative; overflow: hidden;
    box-shadow: 0 3px 8px rgba(0,0,0,0.25);
  }
  .card-front {
    background: var(--card-black);
    display: flex; align-items: center; justify-content: center;
  }
  .front-wordmark {
    color: var(--emboss); font-weight: 600; font-size: 72px; letter-spacing: 1px;
  }
  .card-back { background: var(--card-white); }
  .back-band {
    position: absolute; left: 0; top: 0; width: 100%; height: 158px;
    background: var(--card-black);
  }
  .back-wordmark {
    position: absolute; left: 26px; top: 78px;
    display: flex; align-items: center; gap: 10px;
    color: var(--ink-light); font-weight: 600; font-size: 34px;
  }
  .back-wordmark .mark-dot {
    width: 14px; height: 14px; border-radius: 50%; background: var(--ink-light);
  }
  .holder {
    position: absolute; left: 232px; top: 102px; color: var(--ink-light);
  }
  .holder-name { font-weight: 600; font-size: 17px; line-height: 1.2; }
  .holder-title { font-size: 12px; line-height: 1.4; }
  .contact {
    position: absolute; left: 232px; top: 176px; color: var(--ink-dark);
    font-size: 12.5px; line-height: 1.45; list-style: none;
  }
  .contact li { display: flex; align-items: center; gap: 6px; }
  .contact .address { padding-left: 0; }
  .contact svg { width: 11px; height: 11px; flex: none; }
  .contact .address + .address { margin-bottom: 2px; }
</style>
</head>
<body>
<main class="stage">
  <section class="card card-front" aria-label="Card front">
    <span class="front-wordmark">Holvern</span>
  </section>

  <section class="card card-back" aria-label="Card back">
    <div class="back-band"></div>
    <div class="back-wordmark"><span class="mark-dot"></span>Holvern</div>
    <div class="holder">
      <p class="holder-name">Daniel Whitcombe</p>
      <p class="holder-title">President</p>
    </div>
    <ul class="contact">
      <li class="address">480 Harbor Line Road, Suite 12</li>
      <li class="address">Eastport, Ohio, 44012</li>
      <li>
        <svg viewBox="0 0 12 12" aria-hidden="true"><path fill="var(--icon)" d="M2.5 1 L4.5 1 L5.2 3.4 L4 4.4 Q5 6.8 7.6 8 L8.6 6.8 L11 7.5 L11 9.5 Q11 11 9.5 11 Q1 10.5 1 2.5 Q1 1 2.5 1 Z"/></svg>
        (555) 302-4418
      </li>
      <li>
        <svg viewBox="0 0 12 12" aria-hidden="true"><rect x="0.75" y="2.25" width="10.5" height="7.5" fill="none" stroke="var(--icon)" stroke-width="1.2"/><path d="M1 2.5 L6 6.5 L11 2.5" fill="none" stroke="var(--icon)" stroke-width="1.2"/></svg>
        daniel@holvern.com
      </li>
      <li>
        <svg viewBox="0 0 12 12" aria-hidden="true"><circle cx="6" cy="6" r="5" fill="none" stroke="var(--icon)" stroke-width="1.1"/><ellipse cx="6" cy="6" rx="2.2" ry="5" fill="none" stroke="var(--icon)" stroke-width="1"/><line x1="1" y1="6" x2="11" y2="6" stroke="var(--icon)" stroke-width="1"/></svg>
        www.holvern.com
      </li>
    </ul>
  </section>
</main>
</body>
</html>
```